Postcard: Live Ever Kinder

Text for front: HOW TO CHANGE THE WORLD IN ONE [note: the word "one" should be underlined] STEPHint: It's up to you...[Note: add arrow or something to indicate "turn over"]Text for back: You're going to spend your entire life with someone you can never get away from. (Guess who?) Wouldn't you rather that person #LiveEverKinder than judgmental or critical? BE the change you want to see! Visit www.LiveEverKinder-hub.com for daily Bright Pebbles and community. PLEASE JOIN US![Note: add logo to left half of back side]Font preference for text: Josefin sans

Target Market(s)

People who would be attracted to Calvera church - unitarian universalist message. It's spiritual without being overtly religious, so the target market is probably early 30s and up but ideally won't turn off Millennials (folks under 30). It should attract attention of people who are open-minded and committed to progressive social change, tired of an atmosphere of hate-mongering and divisiveness.

Requirements
Nice to have
• It would be nice to convey a sense of challenge - there is an idea of "bright pebbles" so something related to fire/sparks is appropriate. This is meant to evoke a deeper, divine love more than a sense of romantic love. This love is more fierce than fluffy! Yet it calls us to be our best selves.
Should not have
• Please avoid excessive pink - just the logo is enough, as this design needs to appeal to men as well as women.

```html
<!DOCTYPE html>
<html lang="en">
<head>
<meta charset="utf-8">
<title>Live Ever Kinder Postcard</title>
<link rel="stylesheet" href="https://fonts.googleapis.com/css2?family=Josefin+Sans:wght@300;400;600&family=Oswald:wght@600&display=swap">
<style>
  :root {
    --backdrop: #2b211c;
    --card: #ffffff;
    --ink: #1a1a1a;
    --pink: #e8588a;
    --pink-soft: #f4b3c8;
    --pink-pale: #fbe3eb;
    --red: #e5412f;
  }
  html, body { margin: 0; padding: 0; overflow: hidden; }
  body {
    width: 1200px; height: 1200px; background: var(--backdrop);
    position: relative; font-family: "Josefin Sans", sans-serif; color: var(--ink);
  }
  .card { position: absolute; background: var(--card); overflow: hidden; }
  .card-front { left: 204px; top: 79px; width: 776px; height: 527px; }
  .card-back { left: 199px; top: 634px; width: 786px; height: 534px; }
  .card-art { position: absolute; inset: 0; width: 100%; height: 100%; }

  .headline {
    position: absolute; left: 64px; width: 680px; text-align: center; margin: 0;
    font-weight: 300; font-size: 72px; line-height: 1; letter-spacing: 0; white-space: nowrap;
  }
  .headline-1 { top: 110px; }
  .headline-2 { top: 197px; }
  .headline-3 { top: 272px; line-height: 100px; }
  .headline .accent {
    display: inline-block; position: relative; margin: 0 6px;
    font-family: "Oswald", sans-serif; font-weight: 600; color: var(--pink);
    font-size: 76px; line-height: 1; letter-spacing: 0;
  }
  .headline .accent::after {
    content: ""; position: absolute; left: -14px; right: -18px; bottom: -12px; height: 3px;
    background: var(--pink); border-radius: 2px; transform: rotate(-2deg);
  }
  .hint { position: absolute; left: 72px; top: 400px; margin: 0; font-size: 49px; font-weight: 400; white-space: nowrap; }
  .turn-over {
    position: absolute; left: 704px; top: 452px; color: #fff; font-family: "Oswald", sans-serif;
    font-weight: 600; font-size: 16px; line-height: 17px; text-align: center;
  }

  .brand-mark { position: absolute; left: 40px; top: 80px; width: 200px; text-align: center; }
  .brand-dot { width: 130px; height: 130px; border-radius: 50%; background: var(--pink); margin: 0 auto 22px; }
  .brand-name { font-size: 24px; font-weight: 400; color: var(--pink); margin: 0; white-space: nowrap; }

  .message { position: absolute; left: 308px; width: 460px; text-align: center; margin: 0; line-height: 1; white-space: nowrap; }
  .message-lead { font-size: 29px; }
  .message-small { font-size: 18px; }
  .message-body { font-size: 23px; }
  .message-url { font-size: 26px; }
  .message-note { font-size: 19px; }
  .join {
    position: absolute; left: 65px; top: 410px; margin: 0; font-size: 76px; font-weight: 400;
    line-height: 1; white-space: nowrap; letter-spacing: 1px;
  }
  .join .please { color: var(--red); margin-right: 34px; }
</style>
</head>
<body>
  <section class="card card-front">
    <svg class="card-art" viewBox="0 0 776 527" aria-hidden="true">
      <defs>
        <linearGradient id="fade-pattern" x1="0" y1="0" x2="1" y2="0">
          <stop offset="0" stop-color="#fbe3eb" stop-opacity="0"/>
          <stop offset="1" stop-color="#f6c6d6" stop-opacity="0.8"/>
        </linearGradient>
      </defs>
      <rect x="220" y="320" width="520" height="207" fill="url(#fade-pattern)" role="img" aria-label="Faint triangle pattern"/>
      <path d="M776 233 C 740 370 660 470 548 527 L 776 527 Z" fill="var(--pink-soft)"/>
      <path d="M776 330 C 745 420 680 490 600 527 L 776 527 Z" fill="var(--pink)"/>
      <path d="M632 376 H 680 M 662 356 L 684 376 L 662 396" fill="none" stroke="var(--pink-soft)" stroke-width="6"/>
      <path d="M600 390 L 640 430 L 600 470" fill="none" stroke="#f6c6d6" stroke-width="12" opacity="0.7"/>
      <path d="M540 400 L 575 430 L 540 460" fill="none" stroke="#f9d6e2" stroke-width="12" opacity="0.7"/>
      <circle cx="680" cy="451" r="20" fill="#fff"/>
    </svg>
    <h1 class="headline headline-1">HOW TO CHANGE</h1>
    <p class="headline headline-2">THE WORLD</p>
    <p class="headline headline-3">IN <span class="accent">ONE</span> STEP</p>
    <p class="hint">Hint: It's up to you...</p>
    <div class="turn-over">TURN<br>OVER</div>
  </section>

  <section class="card card-back">
    <svg class="card-art" viewBox="0 0 786 534" aria-hidden="true">
      <defs>
        <radialGradient id="wash" cx="0.6" cy="0.45" r="0.7">
          <stop offset="0" stop-color="#ef7fa3"/>
          <stop offset="1" stop-color="#e8588a"/>
        </radialGradient>
      </defs>
      <path d="M282 0 C 220 160 272 400 400 534 L 786 534 L 786 0 Z" fill="url(#wash)" role="img" aria-label="Pink watercolour wash"/>
      <path d="M335 368 Q 540 356 743 362" fill="none" stroke="#fff" stroke-width="3"/>
    </svg>
    <div class="brand-mark">
      <div class="brand-dot"></div>
      <p class="brand-name">Live Ever Kinder</p>
    </div>
    <p class="message message-lead" style="top:40px">You're going to spend</p>
    <p class="message message-lead" style="top:79px">your entire life with someone</p>
    <p class="message message-lead" style="top:117px">you can never get away from.</p>
    <p class="message message-small" style="top:153px">(Guess who?)</p>
    <p class="message message-body" style="top:202px">Wouldn't you rather that person</p>
    <p class="message message-body" style="top:231px">#LiveEverKinder</p>
    <p class="message message-body" style="top:259px">than judgmental or critical?</p>
    <p class="message message-body" style="top:288px">BE the change you want to see!</p>
    <p class="message message-url" style="top:326px">Visit www.LiveEverKinder-hub.com</p>
    <p class="message message-note" style="top:382px">for daily Bright Pebbles and community.</p>
    <p class="join"><span class="please">PLEASE</span>JOIN US!</p>
  </section>
</body>
</html>
```